Tom Verlane

I am the director of Casa Del Humo International. We make premium cigars

I want an insanely beautiful card that directly attracts attention. Do your best. The card can use emboss, foil, laser-cut metal or anything else. Make it stand out, but also elegant.

Target Market(s)

Cigar Distributors

Industry/Entity Type

Cigars

Contact Information for Business Card

Email: tom.verlane@verlanos.com + Logos (attached) + Position: Director + 'High-End Cigars'

Colors

Designer to choose colors to be used in the design.

Requirements
Nice to have
• Please check us out at www.casadelhumo.com and try to use our colors and styles

```html
<!DOCTYPE html>
<html lang="en">
<head>
<meta charset="utf-8">
<title>Casa Del Humo International – Business Card</title>
<link rel="stylesheet" href="https://fonts.googleapis.com/css2?family=EB+Garamond:wght@400;500&family=Arimo:wght@400&display=swap">
<style>
  :root {
    --backdrop: #adadad;
    --card-black: #0e0d0d;
    --card-charcoal: #1c1b1a;
    --gold: #c9a36a;
    --gold-soft: #a88659;
    --ivory: #f4f1ea;
    --crimson: #c4232b;
    --photo-dark: #1f1c19;
    --photo-stone: #5e5848;
    --tobacco: #6b4a31;
  }
  * { margin: 0; padding: 0; box-sizing: border-box; }
  html, body {
    width: 1200px; height: 476px; overflow: hidden;
    background: var(--backdrop);
  }
  .canvas { position: relative; width: 1200px; height: 476px; }

  .card {
    position: absolute;
    width: 548px; height: 313px;
    overflow: hidden;
    background:
      radial-gradient(ellipse 40% 60% at 95% 70%, rgba(255,255,255,0.05), transparent 70%),
      radial-gradient(ellipse 35% 50% at 5% 60%, rgba(255,255,255,0.04), transparent 70%),
      radial-gradient(ellipse 80% 70% at 50% 40%, var(--card-charcoal), var(--card-black));
    box-shadow: 0 6px 14px rgba(0,0,0,0.35);
  }
  .card--front { left: 42px; top: 82px; }
  .card--back  { left: 610px; top: 81px; }

  .frame {
    position: absolute; inset: 17px 20px 18px 20px;
    border: 1px solid var(--gold-soft);
  }
  .frame::after {
    content: ""; position: absolute; inset: 3px;
    border: 1px solid var(--gold-soft);
  }

  .company-name {
    position: absolute; left: 0; right: 0;
    text-align: center;
    font-family: "EB Garamond", serif;
    font-weight: 400;
    color: var(--ivory);
    letter-spacing: 0.01em;
    white-space: nowrap;
  }
  .location {
    position: absolute; left: 0; right: 0;
    text-align: center;
    font-family: "Arimo", Arial, sans-serif;
    font-weight: 400;
    color: var(--ivory);
    white-space: nowrap;
  }
  .rule { position: absolute; }

  /* Front */
  .card--front .company-name { top: 118px; font-size: 22.5px; }
  .card--front .rule { left: 81px; top: 151px; width: 386px; height: 12px; }
  .card--front .location { top: 175px; font-size: 14.5px; }
  .front-photo {
    position: absolute; left: 420px; top: 180px; width: 128px; height: 133px;
    background:
      radial-gradient(ellipse 45% 35% at 72% 30%, var(--photo-stone), transparent 80%),
      radial-gradient(ellipse 70% 40% at 45% 78%, var(--photo-dark), transparent 85%);
    opacity: 0.85;
  }

  /* Back */
  .email {
    position: absolute; left: 0; right: 0; top: 44px;
    text-align: center;
    font-family: "EB Garamond", serif;
    font-weight: 400;
    font-size: 29px; color: var(--ivory);
    white-space: nowrap;
  }
  .role, .tagline {
    position: absolute; left: 0; right: 0;
    text-align: center;
    font-family: "EB Garamond", serif;
    font-weight: 400;
    color: var(--gold);
  }
  .role { top: 82px; font-size: 18px; }
  .card--back .company-name { top: 118px; font-size: 11px; }
  .card--back .rule { left: 177px; top: 133px; width: 193px; height: 8px; }
  .card--back .location { top: 147px; font-size: 7.5px; }
  .tagline { top: 163px; font-size: 18px; }

  .cigar-photo {
    position: absolute; left: 51px; top: 164px; width: 70px; height: 128px;
    background: linear-gradient(90deg, var(--photo-dark), var(--tobacco) 35%, #7a5a3c 65%, var(--tobacco));
    border-radius: 12px 12px 0 0;
  }

  .brand-row {
    position: absolute; left: 178px; top: 242px; width: 192px; height: 24px;
    display: flex; align-items: center; justify-content: space-between;
    font-family: "EB Garamond", serif; font-weight: 400; font-size: 10.5px;
    color: var(--gold);
  }
  .brand-name { white-space: nowrap; }
  .brand-divider { width: 1px; height: 18px; background: rgba(201,163,106,0.5); }
</style>
</head>
<body>
<main class="canvas">

  <section class="card card--front">
    <div class="frame"></div>
    <h1 class="company-name">CASA del HUMO INTERNATIONAL</h1>
    <svg class="rule" viewBox="0 0 386 12" preserveAspectRatio="none" aria-hidden="true">
      <line x1="0" y1="6" x2="386" y2="6" stroke="#c4232b" stroke-width="1.2"/>
      <rect x="188" y="1" width="7" height="7" fill="#c4232b" transform="rotate(45 191.5 6)"/>
    </svg>
    <p class="location">VALDEZA - ORIVELA</p>
    <div class="front-photo" role="img" aria-label="Photo of a gold-veined stone and a wrapped cigar on dark sand"></div>
  </section>

  <section class="card card--back">
    <div class="frame"></div>
    <p class="email">tom.verlane@verlanos.com</p>
    <p class="role">Director</p>
    <h2 class="company-name">CASA del HUMO INTERNATIONAL</h2>
    <svg class="rule" viewBox="0 0 193 8" preserveAspectRatio="none" aria-hidden="true">
      <line x1="0" y1="4" x2="193" y2="4" stroke="#c4232b" stroke-width="1"/>
      <rect x="94" y="1.5" width="5" height="5" fill="#c4232b" transform="rotate(45 96.5 4)"/>
    </svg>
    <p class="location">VALDEZA - ORIVELA</p>
    <p class="tagline">High-End Cigars</p>
    <div class="cigar-photo" role="img" aria-label="Photo of three premium cigars standing upright"></div>
    <div class="brand-row">
      <span class="brand-name">Navigante</span>
      <span class="brand-divider"></span>
      <span class="brand-name">Amber Line</span>
      <span class="brand-divider"></span>
      <span class="brand-name">Serie Carmesí</span>
    </div>
  </section>

</main>
</body>
</html>
```